eBook Cover Design Project - Starlight Letters

We need an ebook cover design for our new digital only title for Driftwood Publishing.
Driftwood Publishing is an exciting new initiative from Moravel Holdings (Australia) that will leverage our expertise in romance to take Australian authors to a global audience.
Driftwood Publishing is Romance. Driftwood will own Romance in digital-first as Moravel owns Romance in print and ebook.
Driftwood Publishing is Your Romance – we’re the publisher that readers go to for the romance that they want to read, in the format they want to read it, when they want to read it. We’re also the first choice publisher for new and existing authors as we are dedicated to making our authors a success through our close connection to our readers, giving us insight into the best way to help publish, market and sell our ebooks.

Target Market(s)

30-55 year old women.

Industry/Entity Type

Digital

Requirements
Must have
• Must work as a black and white image as well as a colour image.
-Must be easily viewed at thumbnail size.
-Title must always be larger than the author name. Both must appear on cover.
-Final file should be a JPEG supplied at 2240 pixels (H) X 1400 pixels (W).
-See attached document for story report.
-If using people on the cover refer to character traits in story report.
Should not have
• Offensive or pornographic content.
-Too many elements – keep it simple.

```html
<!DOCTYPE html>
<html lang="en">
<head>
<meta charset="utf-8">
<title>Starlight Letters – Maren Colby</title>
<link href="https://fonts.googleapis.com/css2?family=Tenor+Sans&display=swap" rel="stylesheet">
<style>
  :root {
    --sky-peach: #efc2a8;
    --sky-rose: #e9a58c;
    --glow-orange: #f39a5a;
    --ember: #e2683a;
    --dusk: #5a3a34;
    --ground: #1f1a1c;
    --canopy: #1c1f1a;
    --title-ink: #111111;
    --author-ink: #ffffff;
    --imprint-ink: #8a8a8a;
    --page: #ffffff;
  }
  * { margin: 0; padding: 0; box-sizing: border-box; }
  html, body {
    width: 750px;
    height: 1200px;
    overflow: hidden;
    background: var(--page);
  }
  .cover {
    position: relative;
    width: 750px;
    height: 1200px;
    overflow: hidden;
    font-family: "Tenor Sans", sans-serif;
  }
  .cover-art {
    position: absolute;
    inset: 0;
    background:
      radial-gradient(ellipse 62% 30% at 48% 18%, rgba(28, 31, 26, 0.85), rgba(28, 31, 26, 0) 100%),
      radial-gradient(ellipse 40% 26% at 50% 38%, rgba(120, 140, 110, 0.45), rgba(120, 140, 110, 0) 100%),
      radial-gradient(ellipse 80% 22% at 50% 98%, rgba(31, 26, 28, 0.95), rgba(31, 26, 28, 0) 100%),
      linear-gradient(180deg,
        var(--sky-peach) 0%,
        var(--sky-rose) 28%,
        var(--glow-orange) 52%,
        var(--ember) 72%,
        var(--dusk) 88%,
        var(--ground) 100%);
  }
  .book-title {
    position: absolute;
    left: 0;
    right: 0;
    top: 752px;
    text-align: center;
    font-size: 61px;
    font-weight: 400;
    letter-spacing: 2px;
    color: var(--title-ink);
    line-height: 1;
    text-transform: uppercase;
    white-space: nowrap;
  }
  .author-name {
    position: absolute;
    left: 0;
    right: 0;
    top: 1076px;
    padding-left: 52px;
    text-align: center;
    font-size: 50px;
    font-weight: 400;
    letter-spacing: 1px;
    color: var(--author-ink);
    line-height: 1;
    text-transform: uppercase;
    white-space: nowrap;
  }
  .imprint {
    position: absolute;
    left: 0;
    right: 0;
    top: 1172px;
    text-align: center;
    font-size: 12px;
    color: var(--imprint-ink);
    line-height: 1;
    letter-spacing: 0.5px;
  }
</style>
</head>
<body>
  <main class="cover">
    <div class="cover-art" role="img" aria-label="Painted silhouette of a large tree strung with glowing coloured Christmas lights against an orange sunset sky, its trunk rising from a snowy mound"></div>
    <h1 class="book-title">Starlight Letters</h1>
    <p class="author-name">Maren Colby</p>
    <p class="imprint">driftwood publishing</p>
  </main>
</body>
</html>
```